Lumo-Vast.com -> We need someone to design a homepage [For Mobile]

We need a graphic design of our homepage for mobile, which will include login and signup. It's only the design we need, we would take care of the coding, so if you're a good designer you're welcome to participate. The Login & Registration page contain a few fields. Login --> Username & Password & Forgot my Password. Registration --> Email, Username, Password. Needs to be a clean design.[Registration in a different page, Login and Homepage in the same one]
Updates

Project Deadline Extended Reason: We're going to consider what we got so far and allow others to submit more designs as well, the final deadline would be this week, we won't extend it again. Added Saturday, December 20, 2014

Project Deadline Extended Reason: Very sorry, we just got more than expected designs and we want to go over all of them in order to make a proper decision - we would extend the project until the 1st of January 2015, this is definitely a FINAL date. Added Friday, December 26, 2014

Industry/Entity Type

Graphic Design

Number of Pages Required

2 page

Requirements
Must have
• * Enclosed our logo to include with the design.
• * Add the following text as well
• WANT TO EARN EXTRA MONEY?
• WITH LUMO-VAST.COM YOU CAN!
• LUMO-VAST.COM. IT'S AS EASY AS 1, 2, 3.
• (1) Register (2) Earn & Win Coins (3) Redeem Coins
• * It must have "Login" and "Register" buttons on the home page.
Nice to have
• [Note: Also to make it easier for you, enclosed a screenshot of the main page in a desktop (PC) view.]

```html
<!DOCTYPE html>
<html lang="en">
<head>
<meta charset="utf-8">
<title>Lumo-Vast.com – Mobile Home</title>
<link href="https://fonts.googleapis.com/css2?family=Arvo:wght@400;700&family=Open+Sans:wght@300;400;600&display=swap" rel="stylesheet">
<style>
  :root {
    --stage: #b9bec3;
    --screen: #dcedf2;
    --panel: #f2f9fb;
    --divider: #cfdde2;
    --green: #1fa45a;
    --green-light: #8cc63f;
    --ink: #3b4a50;
    --ink-dark: #1f3537;
    --muted: #8a9499;
    --white: #ffffff;
  }
  * { box-sizing: border-box; margin: 0; padding: 0; }
  html, body { width: 1200px; height: 1200px; overflow: hidden; }
  body {
    background: var(--stage);
    font-family: "Open Sans", sans-serif;
    color: var(--ink);
    display: flex; align-items: center; justify-content: center;
  }
  .screen {
    position: relative;
    width: 600px; height: 1067px;
    background: var(--screen);
    overflow: hidden;
  }
  .status-bar {
    height: 34px; padding: 0 14px;
    display: flex; align-items: center; justify-content: space-between;
    font-size: 16px; color: #222;
  }
  .status-bar .time { font-weight: 600; }
  .battery { width: 30px; height: 13px; border: 1.5px solid #222; border-radius: 3px; padding: 1px; }
  .battery span { display: block; height: 100%; background: #222; border-radius: 1px; }

  .brand {
    display: flex; align-items: center; justify-content: center; gap: 18px;
    margin-top: 60px;
  }
  .brand-dot { width: 70px; height: 70px; border-radius: 50%; background: var(--green-light); }
  .brand-name { font-size: 58px; font-weight: 400; color: var(--ink); letter-spacing: -1px; }

  .intro { text-align: center; margin-top: 44px; font-family: "Arvo", serif; }
  .intro h1 { font-size: 27px; font-weight: 700; color: var(--green); letter-spacing: 0.5px; }
  .intro p { font-size: 19px; color: var(--ink-dark); line-height: 1.35; margin-top: 8px; }
  .intro a { color: var(--green); text-decoration: none; }

  .steps { display: block; margin: 26px auto 0; }
  .steps text { font-family: "Arvo", serif; font-weight: 700; font-size: 13px; fill: var(--green); }

  .login-form {
    margin: 28px 40px 0;
    background: var(--panel);
  }
  .field {
    height: 108px; display: flex; align-items: center; padding-left: 48px; gap: 70px;
    border-bottom: 1px solid var(--divider);
  }
  .field:last-child { border-bottom: none; }
  .field-icon {
    width: 40px; height: 40px; border-radius: 50%;
    display: flex; align-items: center; justify-content: center; flex-shrink: 0;
  }
  .field-icon.user { background: var(--green); }
  .field-icon.lock { background: var(--ink-dark); }
  .field-label { font-size: 26px; font-weight: 300; color: var(--muted); }
  .forgot {
    text-align: right; margin: 12px 40px 0;
    font-family: "Arvo", serif; font-size: 13px; font-weight: 700; color: var(--ink-dark);
  }

  .actions {
    position: relative; display: flex;
    margin: 60px 40px 0; height: 100px; border-radius: 50px; overflow: hidden;
  }
  .btn {
    font-family: "Arvo", serif; font-size: 22px; color: var(--white);
    display: flex; align-items: center; justify-content: center; flex: 1;
  }
  .btn-login { background: var(--green); clip-path: polygon(0 0, 100% 0, 88% 100%, 0 100%); margin-right: -30px; z-index: 1; padding-right: 30px; }
  .btn-register { background: var(--green-light); padding-left: 30px; }
</style>
</head>
<body>
  <main class="screen">
    <div class="status-bar">
      <span class="carrier">●●●○○ Nomo</span>
      <span class="time">11:27 AM</span>
      <span class="battery"><span></span></span>
    </div>

    <header class="brand">
      <span class="brand-dot"></span>
      <span class="brand-name">lumo-vast</span>
    </header>

    <section class="intro">
      <h1>WANT TO EARN EXTRA MONEY?</h1>
      <p>With <a>lumo-vast.com</a> You Can!<br><a>lumo-vast.com</a> It's as easy as 1, 2, 3.</p>
    </section>

    <svg class="steps" width="520" height="90" viewBox="0 0 520 90" aria-label="Steps: Register, Earn and Win Coins, Redeem Coins">
      <line x1="40" y1="45" x2="480" y2="45" stroke="#1fa45a" stroke-width="1.5"/>
      <g fill="#dcedf2" stroke="#1fa45a" stroke-width="2">
        <circle cx="40" cy="45" r="14"/>
        <circle cx="260" cy="45" r="14"/>
        <circle cx="480" cy="45" r="14"/>
      </g>
      <g text-anchor="middle">
        <text x="40" y="50">1</text>
        <text x="260" y="50">2</text>
        <text x="480" y="50">3</text>
        <text x="40" y="82">Register</text>
        <text x="260" y="82">Earn &amp; Win Coins</text>
        <text x="480" y="18">Redeem Coins</text>
      </g>
    </svg>

    <form class="login-form">
      <div class="field">
        <span class="field-icon user">
          <svg width="18" height="18" viewBox="0 0 18 18" fill="none" stroke="#fff" stroke-width="2"><circle cx="9" cy="6" r="3.5"/><path d="M2.5 16c0-3.5 3-5 6.5-5s6.5 1.5 6.5 5z"/></svg>
        </span>
        <span class="field-label">Username</span>
      </div>
      <div class="field">
        <span class="field-icon lock">
          <svg width="18" height="18" viewBox="0 0 18 18" fill="none" stroke="#8cc63f" stroke-width="2"><rect x="3" y="8" width="12" height="8" rx="1"/><path d="M6 8V5.5a3 3 0 0 1 6 0V8"/></svg>
        </span>
        <span class="field-label">Password</span>
      </div>
    </form>
    <p class="forgot">Forgot Password?</p>

    <nav class="actions">
      <span class="btn btn-login">Login</span>
      <span class="btn btn-register">Register</span>
    </nav>
  </main>
</body>
</html>
```